Business card design for new software start-up

This design is for a double-sided, colour business card. The requirements are as follows:
PREVIEW IMAGES:
The preview images of the card should be shown on a white background (i.e. no wood veneers etc).
The preview images for the front and back of the card should be presented top to bottom without overlapping.
OVERALL DESIGN:
Clean, crisp and simple
LOGO COLOURS:
Green - CMYK 50C 100Y (PMS 376)
Grey - CMYK 80K
CARD SIZES:
Trim Size (Card Size) 90mm x 55mm
Margin Size: 80mm x 45mm
Bleed Size: 96mm x 61mm (i.e. 3mm bleed)
The corners of the card should be SQUARE and NOT ROUNDED.
CARD ORIENTATION:
Landscape (i.e. horizontal).
FRONT OF CARD:
- White background
- Lumatrek logo with tag line
- VentoHub logo scaled to a width of 1.25 inches and not as prominent as the Lumatrek logo
- The VentoHub logo should be placed on a plain background, not overlapping any background images
- Details:
Corwin Aldape
Founder and Chief Software Architect
Lumatrek Pty Ltd
Suite 2407, 15-19 Marlow St
Sydney NSW 2000
Australia
M: +61 (0) 555 0142
E: corwin.aldape@lumatrek-example.com
www.lumatrek-example.com
BACK OF CARD
- Lumatrek logo without tag line
- www.lumatrek-example.com
The back of the card should reflect the concept of being ahead of the curve in a simple or abstract way. Some possible ideas are as follows but other creative suggestions will also be considered:
1) A bell curve taking up the entire area, with the Lumatrek logo on the right, near a position ahead of the curve;
2) A graphical, curved arrow with the Lumatrek logo near the top of the arrow;
3) An abstract curve with the Lumatrek logo near the top of the curve.
At least a portion of the background colour should consist of the logo's green colour using colour code CMYK 50C 100Y (PMS 376). For designs that place the logo over a green background, the colour of the dot over the first "i" may be changed so that it is still visible.
SOURCE FILES
Must be in AI format with 2 versions:
(1) With editable texts/fonts to allow for name and address changes in future;
(2) With all text converted to vectors/paths
PRINT FILES
Must be delivered in PDF, TIFF, JPG, EPS and PSD formats
Images should be 300 DPI
Updates
Revision to design for back of card:
The back of the card should also include the web address: www.lumatrek-example.com
At least a portion of the background colour should consist of the logo's green colour. For designs that place the logo over a green background, the colour of the dot over the first "i" may be changed so that it is still visible.
Additional information:
1) The VentoHub logo should be placed on a plain background, not overlapping any background images;
2) The orientation of the card should be landscape (i.e. horizontal).

```html
<!DOCTYPE html>
<html lang="en">
<head>
<meta charset="utf-8">
<title>Lumatrek Business Card</title>
<link rel="stylesheet" href="https://fonts.googleapis.com/css2?family=Open+Sans:wght@400;700;800&display=swap">
<style>
  :root {
    --brand-green: #8cc63f;
    --pale-green: #bddb8e;
    --brand-grey: #58585a;
    --ink: #3c3c3c;
    --paper: #ffffff;
    --page: #ffffff;
    --edge: #d4d4d4;
  }
  * { box-sizing: border-box; margin: 0; padding: 0; }
  html, body {
    width: 1200px; height: 900px; overflow: hidden;
    background: var(--page);
    font-family: "Open Sans", Arial, sans-serif;
    color: var(--ink);
  }
  .canvas { position: relative; width: 1200px; height: 900px; }
  .card {
    position: absolute; left: 270px; width: 660px;
    background: var(--paper); overflow: hidden;
    border: 1px solid var(--edge);
  }
  .card--front { top: 54px; height: 374px; }
  .card--back { top: 464px; height: 376px; }
  .card__waves { position: absolute; inset: 0; width: 100%; height: 100%; }

  .wordmark {
    position: absolute; font-weight: 800; color: var(--brand-grey);
    letter-spacing: -2px; line-height: 1;
  }
  .card--front .wordmark { left: 36px; top: 34px; font-size: 60px; }
  .card--back .wordmark { left: 96px; top: 176px; font-size: 70px; }

  .tagline {
    position: absolute; font-weight: 400; color: var(--brand-grey);
    font-size: 12px; line-height: 16px; letter-spacing: 1.5px;
  }
  .tagline strong { font-weight: 700; color: var(--ink); }
  .card--front .tagline { left: 366px; top: 58px; }
  .card--back .tagline { left: 470px; top: 196px; }

  .person { position: absolute; left: 36px; top: 232px; }
  .person__name { font-size: 19px; font-weight: 700; color: var(--ink); }
  .person__role { font-size: 10.5px; margin-top: 2px; }

  .contact { position: absolute; left: 356px; top: 184px; font-size: 14.5px; line-height: 24px; color: var(--ink); }
  .contact__company { font-weight: 700; }
  .contact__lines { margin-bottom: 32px; }
  .contact__row { display: flex; align-items: center; gap: 8px; font-size: 14px; }
  .contact__icon { width: 14px; height: 14px; flex: none; }

  .web-address {
    position: absolute; left: 96px; top: 252px;
    font-size: 22px; font-weight: 700; color: var(--brand-grey);
  }
</style>
</head>
<body>
<main class="canvas">

  <section class="card card--front" aria-label="Card front">
    <svg class="card__waves" viewBox="0 0 660 374" preserveAspectRatio="none" aria-hidden="true">
      <path fill="var(--brand-green)" d="M0,196 C150,140 300,116 420,146 C520,170 600,106 660,82 L660,374 L0,374 Z"/>
      <path fill="var(--pale-green)" stroke="var(--paper)" stroke-width="4" d="M0,214 C150,160 300,134 420,164 C520,188 600,124 660,100 L660,376 L0,376 Z"/>
    </svg>
    <div class="wordmark">Lumatrek</div>
    <p class="tagline">BUILDING<br><strong>TOMORROW'S CODE</strong></p>

    <div class="person">
      <p class="person__name">Corwin Aldape</p>
      <p class="person__role">Founder and Chief Software Architect</p>
    </div>

    <div class="contact">
      <div class="contact__lines">
        <p class="contact__company">Lumatrek Pty Ltd</p>
        <p>Suite 2407, 15-19 Marlow St</p>
        <p>Sydney NSW 2000 Australia</p>
      </div>
      <p class="contact__row">
        <svg class="contact__icon" viewBox="0 0 14 14" aria-hidden="true"><rect x="3" y="1" width="8" height="12" rx="1.5" fill="none" stroke="var(--brand-green)" stroke-width="1.6"/><circle cx="7" cy="10.5" r="0.9" fill="var(--brand-green)"/></svg>
        +61 (0) 555 0142
      </p>
      <p class="contact__row">
        <svg class="contact__icon" viewBox="0 0 14 14" aria-hidden="true"><rect x="1" y="3" width="12" height="8.5" fill="none" stroke="var(--brand-green)" stroke-width="1.5"/><path d="M1,3 L7,8 L13,3" fill="none" stroke="var(--brand-green)" stroke-width="1.5"/></svg>
        corwin.aldape@lumatrek-example.com
      </p>
    </div>
  </section>

  <section class="card card--back" aria-label="Card back">
    <svg class="card__waves" viewBox="0 0 660 376" preserveAspectRatio="none" aria-hidden="true">
      <rect width="660" height="376" fill="var(--brand-grey)"/>
      <path fill="var(--brand-green)" d="M0,128 C150,86 320,56 440,96 C540,128 600,78 660,58 L660,376 L0,376 Z"/>
      <path fill="var(--pale-green)" stroke="var(--paper)" stroke-width="4" d="M0,146 C150,104 320,74 440,114 C540,146 600,96 660,76 L662,378 L-2,378 Z"/>
    </svg>
    <div class="wordmark">Lumatrek</div>
    <p class="tagline">BUILDING<br><strong>TOMORROW'S CODE</strong></p>
    <p class="web-address">www.lumatrek-example.com</p>
  </section>

</main>
</body>
</html>
```